依頼詳細
<取扱商品>
レディースバレエシューズ・ルームシューズ・除菌スプレー・マスクケースなど

<ターゲット>
やや女性向け
基本は老若男女問わず

<使用画像について>
商品画像はコンペ終了後にお渡ししますので仮の画像を入れていただければと思います。
商品画像以外の使用素材は有料のものでも問題は有りませんが、quilva picsまたは低価格(0~2000円程度)のものでお願いします。
※もし有料素材を使う場合は最初から購入して頂く必要はないのでウォーターマーク付きのもので提案していただければ大丈夫です。

<デザイン>
明るめのやさしい感じでお願いします。
参考サイトほどピンクは強めでなくてもいいかと思いますが、デザイン次第では濃い色の使用もありかと思います。

参考サイト
https://pelrovin.jp/

<ページ幅>
1920pxでお願いします。

<特筆事項>
今回NIVOを使用するにあたりプラン的にNIVOマークが必須になります。
右上のテントのマークはありきでお願いします。

今後も定期的にデザインをお願いすることができる技量を持つ方を探しておりますので是非、単発と考えずにデザインを出していただければと思います。
それでは皆様のご応募よろしくお願い致します。
サイトURL
ページ数
1ページ
希望イメージ
シンプル 複雑
単色 カラフル
暗い 明るい
日常 高級
遊び心 厳粛
未来的 伝統的
女性的 男性的
希望する色
白・淡いピンク・淡い水色などの優しい色
納品ファイル
• フォトショップ形式 (.psd)
補足説明
■ 選んだ理由

こちらが想定した以上のデザインでした。

■ 提案者全員のお礼・コメント

この度は当方コンペにご提案いただきありがとうございました。
提案頂いた方々のデザインはどれも素敵なもので、真剣に吟味し当選者を選択させていただきました。
今後もミルトカを利用してのデザインコンペを行う予定ですので、残念ながら今回は当選とならなかった方もまたご参加いただけると幸いです。
今後もどうかよろしくお願い致します。

```html
<!DOCTYPE html>
<html lang="ja">
<head>
<meta charset="utf-8">
<title>lumeno</title>
<link href="https://fonts.googleapis.com/css2?family=Noto+Sans+JP:wght@300;400;500&family=Noto+Serif+JP:wght@400&display=swap" rel="stylesheet">
<style>
:root{
  --bg:#fbf1f1;
  --ink:#3a3a3a;
  --muted:#8a8a8a;
  --pink:#f3dede;
  --pink-deep:#e8c6c6;
  --line:#cfcfcf;
  --white:#ffffff;
  --photo-a:#e9ecee;
  --photo-b:#cfd4d7;
}
*{margin:0;padding:0;box-sizing:border-box}
html,body{width:1200px;height:2584px;overflow:hidden}
body{background:var(--bg);color:var(--ink);font-family:"Noto Sans JP",sans-serif;position:relative}

.site-header{position:absolute;left:0;top:0;width:1200px;height:120px}
.logo{position:absolute;left:76px;top:34px;font-family:"Noto Serif JP",serif;font-size:40px;letter-spacing:1px;color:var(--ink)}
.global-nav{position:absolute;right:80px;top:52px;display:flex;align-items:center;gap:26px;font-size:11px}
.global-nav a{color:var(--ink);text-decoration:none}
.global-nav a.current{border-bottom:1px solid var(--ink);padding-bottom:3px}

.hero{position:absolute;left:130px;top:152px;width:942px;height:548px;background:linear-gradient(180deg,var(--photo-a),#f4f5f6 55%,var(--photo-b))}
.hero-title{position:absolute;right:40px;top:54px;font-family:"Noto Serif JP",serif;font-size:30px;color:var(--ink)}
.hero-sub{position:absolute;right:40px;top:146px;text-align:right}
.hero-sub h2{font-weight:400;font-size:22px;letter-spacing:2px}
.hero-sub p{font-size:15px;margin-top:18px;letter-spacing:1px}
.hero-tile{position:absolute;top:340px;width:116px;height:148px;background:var(--white);opacity:.9}

.sdgs{position:absolute;left:132px;top:768px;width:940px;height:192px;background:var(--white);border:6px solid #e6e6e6}
.sdgs-badge{position:absolute;left:26px;top:66px;width:40px;height:40px;border-radius:50%;background:#d9cfc6}
.sdgs-title{position:absolute;left:76px;top:74px;font-size:17px;letter-spacing:1px}
.sdgs-text{position:absolute;left:286px;top:34px;width:620px;font-size:9px;line-height:20px;color:#555}

.flora{position:absolute;background:radial-gradient(ellipse at center,rgba(226,170,170,.35),rgba(226,170,170,0) 70%)}

.products-head{position:absolute;left:260px;top:1080px;width:336px;height:332px;text-align:center}
.products-head h2{font-weight:400;font-size:22px;margin-top:84px;letter-spacing:2px}
.products-head .rule{width:1px;height:56px;background:var(--muted);margin:18px auto 14px}
.products-head span{font-size:10px;color:var(--muted)}

.card{position:absolute;width:336px;height:332px;background:var(--pink)}
.card .thumb{height:264px;background:linear-gradient(160deg,#eef1f3,#c9cfd4)}
.card .label{height:68px;display:flex;align-items:center;justify-content:center;font-size:18px;letter-spacing:1px}
.card.all{display:flex;flex-direction:column;align-items:center;justify-content:center;background:var(--pink-deep);text-decoration:none;color:var(--ink)}
.card.all p{font-size:17px;letter-spacing:1px}
.card.all .more{display:flex;align-items:center;gap:8px;font-size:10px;margin-top:20px;color:#555}
.card.all .more i{display:block;width:80px;height:1px;background:#555}

.footer-links{position:absolute;left:0;top:2214px;width:1200px;display:flex;justify-content:center}
.footer-link{width:268px;text-align:center;font-size:11px;color:var(--ink)}
.footer-link + .footer-link{border-left:1px solid var(--line)}
.footer-link svg{display:block;margin:0 auto 14px}

.footer-rule{position:absolute;left:0;top:2402px;width:1200px;height:1px;background:var(--line)}
.to-top{position:absolute;left:914px;top:2372px;width:44px;height:44px;border-radius:50%;background:var(--pink-deep);font-size:10px;display:flex;align-items:center;justify-content:center;color:#7a5555}
.footer-meta{position:absolute;top:2440px;font-size:8px;color:var(--muted)}
</style>
</head>
<body>

<header class="site-header">
  <div class="logo">lumeno</div>
  <nav class="global-nav">
    <a class="current" href="#">会社概要</a>
    <a href="#">商品一覧</a>
    <a href="#">よくある質問</a>
    <a href="#">お問い合わせ</a>
    <svg width="14" height="14" viewBox="0 0 14 14" aria-label="マイページ"><circle cx="7" cy="4" r="3" fill="#3a3a3a"/><path d="M1 14c0-4 3-6 6-6s6 2 6 6z" fill="#3a3a3a"/></svg>
    <svg width="16" height="14" viewBox="0 0 16 14" aria-label="カート"><path d="M0 1h3l2 8h9l2-6H4" fill="none" stroke="#3a3a3a" stroke-width="1.6"/><circle cx="6" cy="12" r="1.4" fill="#3a3a3a"/><circle cx="13" cy="12" r="1.4" fill="#3a3a3a"/></svg>
  </nav>
</header>

<section class="hero" role="img" aria-label="白いタイルの壁と観葉植物の鉢がある明るい室内写真">
  <div class="hero-title">lumeno</div>
  <div class="hero-sub">
    <h2>サステナビリティ</h2>
    <p>わたしたちは自然環境に配慮した企業です。</p>
  </div>
  <div class="hero-tile" style="left:414px"></div>
  <div class="hero-tile" style="left:578px"></div>
  <div class="hero-tile" style="left:734px"></div>
</section>

<section class="sdgs">
  <div class="sdgs-badge"></div>
  <div class="sdgs-title">SDGsへの取り組み</div>
  <p class="sdgs-text">私たちは日々の暮らしに寄り添う商品づくりを通して、環境への負担を減らす取り組みを進めています。素材の選定から梱包まで、できることを一つずつ見直しています。長く使える品質と、地球にやさしい選択を大切にし、持続可能な社会の実現に向けて歩み続けます。これからも皆さまと共に、未来につながるものづくりを続けてまいります。</p>
</section>

<div class="flora" role="img" aria-label="淡いピンクの植物の線画" style="left:50px;top:1150px;width:220px;height:290px"></div>
<div class="flora" role="img" aria-label="淡いピンクの植物の線画" style="left:880px;top:1750px;width:260px;height:340px"></div>

<section class="products">
  <div class="products-head">
    <h2>商品</h2>
    <div class="rule"></div>
    <span>Products</span>
  </div>
  <article class="card" style="left:600px;top:1080px">
    <div class="thumb" role="img" aria-label="バレーシューズの商品写真"></div>
    <div class="label">バレーシューズ</div>
  </article>
  <article class="card" style="left:260px;top:1416px">
    <div class="thumb" role="img" aria-label="ルームシューズの商品写真" style="background:linear-gradient(160deg,#f2f2f3,#8a8f98)"></div>
    <div class="label">ルームシューズ</div>
  </article>
  <article class="card" style="left:600px;top:1416px">
    <div class="thumb" role="img" aria-label="抗ウイルス除菌スプレーの商品写真" style="background:linear-gradient(160deg,#ffffff,#dfe3e0)"></div>
    <div class="label">抗ウイルス除菌スプレー</div>
  </article>
  <article class="card" style="left:260px;top:1756px">
    <div class="thumb" role="img" aria-label="マスクケースの商品写真" style="background:linear-gradient(160deg,#ffffff,#dfe3e0)"></div>
    <div class="label">マスクケース</div>
  </article>
  <a class="card all" style="left:600px;top:1756px" href="#">
    <p>全ての商品を見る</p>
    <div class="more">All Items <i></i></div>
  </a>
</section>

<nav class="footer-links">
  <div class="footer-link">
    <svg width="40" height="44" viewBox="0 0 40 44" fill="none" stroke="#3a3a3a" stroke-width="1.6"><rect x="6" y="4" width="28" height="38"/><path d="M12 12h4M20 12h4M12 20h4M20 20h4M12 28h4M20 28h4M17 42v-8h6v8"/></svg>
    会社概要
  </div>
  <div class="footer-link">
    <svg width="46" height="44" viewBox="0 0 46 44" fill="none" stroke="#3a3a3a" stroke-width="1.6"><rect x="4" y="10" width="38" height="26"/><path d="M4 10l19 15 19-15"/></svg>
    お問い合わせ
  </div>
  <div class="footer-link">
    <svg width="46" height="44" viewBox="0 0 46 44" fill="none" stroke="#3a3a3a" stroke-width="1.6"><path d="M8 6h24v18H18l-7 6v-6H8z"/><path d="M24 28h14v10h-3v4l-5-4h-6z"/><path d="M17 12a3 3 0 1 1 4 3v3"/></svg>
    よくある質問
  </div>
</nav>

<div class="footer-rule"></div>
<div class="to-top">TOP</div>
<div class="footer-meta" style="left:140px">Copyright © lumeno All Rights Reserved.</div>
<div class="footer-meta" style="left:330px">プライバシーポリシー</div>
<div class="footer-meta" style="left:450px">特定商取引法に基づく表記</div>

</body>
</html>
```